College Advising Business Card Design

We need a business card design for a new company. We advise students and their families on finding the right colleges to apply to; the application process; creating resumes; writing essays; and once students are accepted, figuring out what the best fit is. We pride ourselves on highly personal service, and we travel the country to learn about schools. The visual we have used on our website is a picture of a graduation caps tossed into the blue sky. See my website.

Target Market(s)

Parents of high school students

Industry/Entity Type

Travel

Contact Information for Business Card

COLLEGE IS THE DREAM. LET US HELP YOU FIND THE DESTINATION.

Marta Delvecchi Ornbrook and Associates
College Admissions Advising and Essay Guidance
enroll@martadelvecchiornbrook.example
555-418-PATH (7284)
Follow us on Campusly

```html
<!DOCTYPE html>
<html lang="en">
<head>
<meta charset="utf-8">
<title>Ornbrook and Associates – Business Card</title>
<link href="https://fonts.googleapis.com/css2?family=PT+Sans:wght@400;700&display=swap" rel="stylesheet">
<style>
  :root {
    --sky-top: #86c6ee;
    --sky-mid: #3f9be3;
    --sky-deep: #1572cf;
    --headline: #1d4f8c;
    --ink: #0f2446;
    --swoosh: #ffffff;
    --social-mark: #3b5ea8;
    --page: #ffffff;
    --photo-warm: #c98a5a;
    --photo-green: #2f9a5a;
    --photo-red: #c8323a;
    --photo-denim: #3a4f78;
  }
  * { margin: 0; padding: 0; box-sizing: border-box; }
  html, body {
    width: 1200px;
    height: 720px;
    overflow: hidden;
    background: var(--page);
  }
  .card {
    position: relative;
    width: 1200px;
    height: 720px;
    overflow: hidden;
    background: linear-gradient(180deg, var(--sky-top) 0%, var(--sky-mid) 45%, var(--sky-deep) 100%);
    font-family: "PT Sans", sans-serif;
  }
  .card__swoosh {
    position: absolute;
    inset: 0;
  }
  .card__headline {
    position: absolute;
    left: 46px;
    top: 56px;
    color: var(--headline);
    font-size: 44px;
    line-height: 62px;
    font-weight: 400;
    letter-spacing: 0.2px;
    text-transform: uppercase;
  }
  .card__social {
    position: absolute;
    right: 48px;
    top: 52px;
    display: flex;
    align-items: center;
    gap: 12px;
    color: var(--social-mark);
    font-size: 30px;
    font-weight: 700;
  }
  .card__social-square {
    width: 34px;
    height: 34px;
    border-radius: 6px;
    background: var(--social-mark);
  }
  .card__photo {
    position: absolute;
    left: 585px;
    top: 285px;
    width: 600px;
    height: 435px;
    border-radius: 180px 160px 0 0;
    background:
      radial-gradient(ellipse at 25% 40%, var(--photo-warm) 0%, transparent 45%),
      radial-gradient(ellipse at 60% 45%, var(--photo-green) 0%, transparent 40%),
      radial-gradient(ellipse at 85% 45%, var(--photo-red) 0%, transparent 40%),
      linear-gradient(180deg, #8c6a55 0%, var(--photo-denim) 100%);
    opacity: 0.92;
  }
  .contact {
    position: absolute;
    left: 52px;
    top: 438px;
    color: var(--ink);
  }
  .contact__name {
    font-size: 37px;
    line-height: 44px;
    margin-bottom: 18px;
  }
  .contact__line {
    font-size: 29px;
    line-height: 44px;
  }
</style>
</head>
<body>
  <main class="card">
    <svg class="card__swoosh" width="1200" height="720" viewBox="0 0 1200 720" aria-hidden="true">
      <defs>
        <linearGradient id="swooshFade" x1="0" y1="0" x2="1" y2="0">
          <stop offset="0" stop-color="#ffffff" stop-opacity="0.95"/>
          <stop offset="0.55" stop-color="#ffffff" stop-opacity="0.9"/>
          <stop offset="1" stop-color="#ffffff" stop-opacity="0.6"/>
        </linearGradient>
        <linearGradient id="swooshEdge" x1="0" y1="0" x2="0" y2="1">
          <stop offset="0" stop-color="#1a5fb8" stop-opacity="0.5"/>
          <stop offset="1" stop-color="#1a5fb8" stop-opacity="0"/>
        </linearGradient>
      </defs>
      <path d="M0 560 C 240 520, 520 600, 820 690 L 860 720 L 0 720 Z" fill="url(#swooshEdge)"/>
      <path d="M0 585 C 260 548, 540 620, 840 720 L 0 720 Z" fill="url(#swooshFade)"/>
    </svg>

    <h1 class="card__headline">College is the dream.<br>Let us help you find the destination.</h1>

    <div class="card__social">
      <span class="card__social-square"></span>
      <span>Campusly</span>
    </div>

    <div class="card__photo" role="img" aria-label="Photo of four smiling college students standing together holding books, folders and backpacks"></div>

    <address class="contact" style="font-style: normal;">
      <p class="contact__name">Marta Delvecchi</p>
      <p class="contact__line">Ornbrook and Associates College</p>
      <p class="contact__line">Admissions Advising and Essay Guidance</p>
      <p class="contact__line">enroll@martadelvecchiornbrook.example</p>
      <p class="contact__line">555-418-PATH (7284)</p>
    </address>
  </main>
</body>
</html>
```